Riverbend Trusted Home Care-Flyer for Patients

Our Home Health Care Agency, Riverbend Trusted Home Care, is seeking a flyer to advertise our services. We would like our flyer to convey professionalism, classiness and sophistication. We want our agency to come across as one that is well-established and recognized as being first-rate within the field.

We also want to appear original; we want to stand out.

Our theme colors, blue and green, from our logo should be incorporated into the flyer's design (refer below).

The top of the page should say (in a clear, bold font)-Seeking Care for your Loved One?

Our Logo, followed by our slogan, "Lean On Those Nearby", should be in the center. (This should make it appear as if our agency is the obvious solution to the consumer's quest in finding suitable care for their family member). This should be in a big font.
Below that, our agency's services should be listed in a very noticeable font...yet smaller than what's written above that.
The text should read:
Our Services Include:
*Experienced Certified Home Health Aides/ Live In Home Health Aides/Companions
*Nursing Services
*Alzheimer’s and Dementia Care
*Respite Care
*Postoperative Care
*Post Rehabilitation Care
*Running Errands
*Light Housekeeping
*Assistance with Bathing, Feeding and Grooming
*Meal Preparation
*Laundry and Linen Washing
*Mail and Bill Organization
*Medication Management
*Accompanying to Doctor’s Appointments
*And much more!
Below that, in a smaller, yet noticeable font:
As seasoned professionals, we know how to help our clients navigate and fulfill their various health care needs. Those nearby are here to help you get the attention that you merit.
Call Riverbend Trusted Home Care today to learn more about our first-rate services!
Below that, in a larger font, our phone number, website, our e-mail address.
*Out contact information will be provided to the project’s winner*.

*Pictures of Caregivers helping elderly patient should be included in the advertisement as well. *

We provided advertisements of other Home Health Care Agencies attached below to use as a reference. Once again, while we are aiming for a similar idea; however, our goal is to stand out as the community's premiere home health care agency, the one that they want to choose. We want to be original as well!

Size: Standard Computer Paper Size. 8.5” x 11”.

Feel free to utilize your creative, designer flair!
We look forward to seeing the results!
Good luck!

Industry/Entity Type

Home Health Care

Font styles to use
Sans Serif

Requirements
Must have
• Refer above.
Nice to have
• Refer to attachment below to see how other home health care agencies advertise. While we are aiming for a similar idea, we would like to incorporate our logo, slogan and colors to make this flyer more unique and stand out. We would like to appear original.

```html
<!DOCTYPE html>
<html lang="en">
<head>
<meta charset="utf-8">
<title>Riverbend Trusted Home Care – Flyer</title>
<link rel="stylesheet" href="https://fonts.googleapis.com/css2?family=PT+Sans:wght@400;700&display=swap">
<style>
  :root {
    --navy: #252c6a;
    --navy-deep: #1d2358;
    --green: #7fc241;
    --light-gray: #e8e9ec;
    --white: #ffffff;
  }
  html, body {
    margin: 0;
    padding: 0;
    width: 989px;
    height: 1200px;
    overflow: hidden;
    background: var(--white);
  }
  .flyer {
    position: relative;
    width: 989px;
    height: 1200px;
    overflow: hidden;
    background: var(--light-gray);
    font-family: "PT Sans", sans-serif;
    color: var(--white);
  }
  .hero-photo {
    position: absolute;
    left: 0; top: 0;
    width: 989px; height: 620px;
    background:
      radial-gradient(ellipse 340px 260px at 200px 210px, #ffffff 0%, rgba(255,255,255,.95) 45%, rgba(255,255,255,0) 100%),
      linear-gradient(120deg, #d9cfa8 0%, #8f8a4c 30%, #5f6c35 50%, #9fb2d6 66%, #e9e1d6 78%, #6b7a3c 100%);
  }
  .shapes {
    position: absolute;
    left: 0; top: 0;
    width: 989px; height: 1200px;
  }
  .brand {
    position: absolute;
    left: 44px; top: 150px;
    color: var(--navy);
  }
  .brand-dot {
    width: 70px; height: 70px;
    border-radius: 50%;
    background: var(--navy);
    margin: 0 0 14px 150px;
  }
  .brand-name {
    font-size: 27px;
    font-weight: 700;
    text-transform: uppercase;
    letter-spacing: .5px;
    line-height: 1;
  }
  .brand-tagline {
    margin-top: 8px;
    font-size: 12px;
    font-weight: 700;
    letter-spacing: 4.2px;
    text-transform: uppercase;
    border-top: 2px solid var(--green);
    padding-top: 5px;
  }
  .kicker {
    position: absolute;
    left: 37px; top: 508px;
    margin: 0;
    font-size: 21px;
    font-weight: 700;
    color: var(--green);
    text-transform: uppercase;
  }
  .headline {
    position: absolute;
    left: 37px; top: 546px;
    margin: 0;
    font-size: 56px;
    line-height: 65px;
    font-weight: 700;
    text-transform: uppercase;
    text-shadow: 2px 3px 6px rgba(0,0,0,.35);
  }
  .headline .accent { color: var(--green); }
  .headline-rule {
    position: absolute;
    left: 37px; top: 766px;
    width: 157px; height: 5px;
    background: var(--green);
  }
  .intro {
    position: absolute;
    left: 37px; top: 800px;
    width: 418px;
    margin: 0;
    font-size: 14.5px;
    line-height: 20px;
    text-align: justify;
  }
  .services {
    position: absolute;
    left: 509px; top: 558px;
    width: 460px;
    margin: 0; padding: 0;
    list-style: none;
    font-size: 16px;
    line-height: 21.5px;
  }
  .services li {
    position: relative;
    padding-left: 22px;
  }
  .services li::before {
    content: "";
    position: absolute;
    left: 0; top: 5px;
    width: 12px; height: 12px;
    border-radius: 50%;
    background: var(--green);
  }
  .services li::after {
    content: "";
    position: absolute;
    left: 3px; top: 8.5px;
    width: 3.5px; height: 3.5px;
    border-top: 1.6px solid var(--navy);
    border-right: 1.6px solid var(--navy);
    transform: rotate(45deg);
  }
  .care-photo {
    position: absolute;
    top: 913px;
    width: 164px; height: 164px;
    border-radius: 50%;
    border: 4px solid var(--white);
    box-sizing: border-box;
    box-shadow: 0 2px 6px rgba(0,0,0,.25);
  }
  .care-photo--visit { left: 233px; background: linear-gradient(135deg, #e7e4df, #7a8aa3 50%, #6b4b3a); }
  .care-photo--comfort { left: 403px; background: linear-gradient(135deg, #dfe3e8, #c8b9ae 50%, #8c94a6); }
  .care-photo--housekeeping { left: 573px; background: linear-gradient(135deg, #f1ede4, #d8c08a 55%, #3b3b3b); }
  .cta {
    position: absolute;
    left: 0; top: 1108px;
    width: 989px;
    margin: 0;
    text-align: center;
    font-size: 18px;
    font-weight: 700;
    color: var(--navy);
    text-transform: uppercase;
  }
  .contacts {
    position: absolute;
    left: 0; top: 1146px;
    width: 989px;
    font-size: 18px;
    color: var(--navy);
  }
  .contact {
    position: absolute;
    display: flex;
    align-items: center;
    gap: 8px;
  }
  .contact--email { left: 44px; }
  .contact--phone { left: 448px; }
  .contact--web { left: 666px; }
  .contact-icon {
    width: 18px; height: 18px;
    flex: none;
  }
</style>
</head>
<body>
<main class="flyer">
  <div class="hero-photo" role="img" aria-label="Photo of a smiling caregiver in blue scrubs hugging a seated elderly woman outdoors"></div>

  <svg class="shapes" viewBox="0 0 989 1200" aria-hidden="true">
    <path d="M0 372 C260 392 620 430 989 532 L989 552 C620 452 260 406 0 392 Z" fill="var(--green)"/>
    <path d="M0 404 C260 416 620 462 989 566 L989 1012 C720 1060 420 985 0 938 Z" fill="var(--navy)"/>
    <path d="M0 938 C160 950 300 968 420 985 L420 1000 C300 990 160 978 0 980 Z" fill="var(--green)"/>
    <path d="M650 1040 C780 1035 900 1020 989 1000 L989 1016 C900 1040 780 1050 650 1040 Z" fill="#b9bcc6"/>
  </svg>

  <div class="brand">
    <div class="brand-dot"></div>
    <div class="brand-name">Riverbend Trusted Home Care</div>
    <div class="brand-tagline">Lean On Those Nearby</div>
  </div>

  <p class="kicker">Seeking care for your loved one?</p>
  <h1 class="headline">Lean On<br>Those<br><span class="accent">Nearby</span></h1>
  <div class="headline-rule"></div>
  <p class="intro">As seasoned professionals, we know how to help our clients navigate and fulfill their various health care needs. Those nearby are here to help you get the attention that you merit.</p>

  <ul class="services">
    <li>Experienced Certified Home Health<br>Aides/ Live In Home Health Aides/Companions</li>
    <li>Nursing Services</li>
    <li>Alzheimer’s and Dementia Care</li>
    <li>Respite Care</li>
    <li>Postoperative Care</li>
    <li>Post Rehabilitation Care</li>
    <li>Running Errands</li>
    <li>Light Housekeeping</li>
    <li>Assistance with Bathing, Feeding and Grooming</li>
    <li>Meal Preparation</li>
    <li>Laundry and Linen Washing</li>
    <li>Mail and Bill Organization</li>
    <li>Medication Management</li>
    <li>Accompanying to Doctor’s Appointments</li>
    <li>And much more!</li>
  </ul>

  <div class="care-photo care-photo--visit" role="img" aria-label="Photo of a caregiver checking an elderly man's blood pressure"></div>
  <div class="care-photo care-photo--comfort" role="img" aria-label="Photo of a caregiver comforting an elderly woman"></div>
  <div class="care-photo care-photo--housekeeping" role="img" aria-label="Photo of a gloved hand cleaning a kitchen counter"></div>

  <p class="cta">Call Riverbend Trusted Home Care today to learn more about our first-rate services!</p>

  <div class="contacts">
    <div class="contact contact--email">
      <svg class="contact-icon" viewBox="0 0 18 18"><circle cx="9" cy="9" r="9" fill="var(--green)"/><rect x="4.5" y="6" width="9" height="6.5" rx="1" fill="none" stroke="#fff" stroke-width="1.3"/><path d="M4.8 6.4 L9 9.6 L13.2 6.4" fill="none" stroke="#fff" stroke-width="1.3"/></svg>
      <span>hello@riverbendtrusted.com</span>
    </div>
    <div class="contact contact--phone">
      <svg class="contact-icon" viewBox="0 0 18 18"><circle cx="9" cy="9" r="9" fill="var(--green)"/><path d="M6 4.5 L7.6 4.5 L8.3 6.8 L7.2 7.7 C7.8 9 8.9 10.1 10.2 10.7 L11.1 9.6 L13.4 10.3 L13.4 11.9 C13.4 12.6 12.8 13.2 12.1 13.1 C8.4 12.7 5.2 9.5 4.8 5.8 C4.7 5.1 5.3 4.5 6 4.5 Z" fill="#fff"/></svg>
      <span>1 555 0142</span>
    </div>
    <div class="contact contact--web">
      <svg class="contact-icon" viewBox="0 0 18 18"><circle cx="9" cy="9" r="9" fill="var(--green)"/><circle cx="9" cy="9" r="4.8" fill="none" stroke="#fff" stroke-width="1.2"/><ellipse cx="9" cy="9" rx="2" ry="4.8" fill="none" stroke="#fff" stroke-width="1.1"/><path d="M4.2 9 H13.8" stroke="#fff" stroke-width="1.1"/></svg>
      <span>www.riverbendtrusted.com</span>
    </div>
  </div>
</main>
</body>
</html>
```